Modern Medical Optometry Website

We need mordern, Patient friendly website. Easy to navigate and enhance our advance medical technology and excellent patient care.
1. HOME PAGE
2. OUR TEAM PAGE
3. EYECARE PAGE - VISION SERVICES, EYE EXAMS, KERATOCONUS CENTER, GLAUCOMA , DIABITES, TORVANEX EXAM, DIGITAL RETINAL, OCT.
4. MYOPIA CONTROL CLINIC
5. DRY EYE CLINIC
6. EYEWEAR
7. PATIENT CENTER - BLOG
7. CONTACT US
This is our current website www.brindlecove.com
and We want to add more content and a cleaner design like these website
http://tamsworthoptometry.com/
https://www.klmhaven.com/

```html
<!DOCTYPE html>
<html lang="en">
<head>
<meta charset="utf-8">
<title>Brindle Cove Optometry</title>
<link href="https://fonts.googleapis.com/css2?family=Raleway:wght@300;400;500;600&family=Lato:ital,wght@0,400;0,700;1,400&display=swap" rel="stylesheet">
<style>
:root{
  --yellow:#f9d53b;
  --dark:#2a2a2a;
  --darker:#232323;
  --ink:#222;
  --body:#555;
  --line:#d8d8d8;
  --white:#fff;
}
*{box-sizing:border-box;margin:0;padding:0}
html,body{width:1200px;height:2761px;overflow:hidden}
body{font-family:'Lato',sans-serif;color:var(--ink);background:var(--white);position:relative}
.heading{font-family:'Raleway',sans-serif;font-weight:400;letter-spacing:.5px}
.btn{display:inline-block;background:var(--yellow);color:var(--ink);font-family:'Lato',sans-serif;font-size:10px;letter-spacing:.5px;text-transform:uppercase;padding:9px 18px}
.rule{width:22px;height:2px;background:var(--ink);margin-top:16px}
.ph{display:block}

/* header */
.site-header{position:absolute;top:0;left:0;width:1200px;height:95px}
.brand{position:absolute;left:36px;top:14px;display:flex;align-items:center;gap:8px}
.brand-mark{width:30px;height:30px;background:var(--yellow)}
.brand-name{font-family:'Lato',sans-serif;font-size:13px;font-weight:700;color:#b8970f;line-height:1.1;letter-spacing:1px}
.top-contact{position:absolute;right:40px;top:12px;display:flex;align-items:center;gap:22px;font-size:11px;color:#444}
.top-contact .btn{padding:9px 16px}
.main-nav{position:absolute;right:40px;top:66px;display:flex;gap:24px;font-size:10px;text-transform:uppercase;color:#333}

/* hero */
.hero{position:absolute;top:95px;left:0;width:1200px;height:503px;background:linear-gradient(100deg,#8c8f99 0%,#b7b8be 35%,#dedfe3 60%,#eeeff1 100%)}
.hero-copy{position:absolute;left:38px;top:112px;color:var(--white);width:360px}
.hero-copy h1{font-family:'Raleway',sans-serif;font-weight:400;font-size:42px;line-height:1.08}
.hero-copy p{font-size:13px;line-height:1.45;margin:14px 0 26px}

/* promise row */
.info-row{position:absolute;top:598px;left:0;width:1200px;height:402px;display:flex}
.promise{width:600px;padding:66px 38px}
.promise h2,.hours h2,.find h2{font-size:30px}
.promise p{font-size:10.5px;line-height:1.75;color:var(--body);margin-top:26px}
.promise p+p{margin-top:14px}
.promise .btn{margin-top:26px}
.hours{width:300px;background:var(--yellow);padding:66px 38px;color:var(--ink)}
.hours table{width:100%;margin-top:40px;font-size:10px;border-collapse:collapse}
.hours td{padding:0 0 16px}
.hours td:last-child{text-align:right}
.hours .note{text-align:center;font-size:10px;line-height:1.6;margin-top:30px}
.find{width:300px;background:var(--dark);color:var(--white);padding:66px 38px}
.find .rule{background:var(--white)}
.find ul{list-style:none;margin-top:24px;font-size:10.5px;line-height:1.45}
.find li{display:flex;gap:10px;margin-bottom:12px}
.find .btn{margin-top:8px}

/* service grid */
.services{position:absolute;top:1000px;left:0;width:1200px;height:442px;display:grid;grid-template-columns:repeat(4,300px);grid-template-rows:repeat(2,221px)}
.tile{display:flex;align-items:center;justify-content:center;padding:16px}
.tile-card{width:100%;height:100%;border:1px solid var(--line);display:flex;align-items:center;justify-content:center;text-align:center;font-family:'Raleway',sans-serif;font-size:29px;line-height:1.05;text-transform:uppercase}

/* patient center */
.patient-center{position:absolute;top:1442px;left:0;width:1200px;height:176px;background:var(--yellow);padding:0 38px;display:flex;align-items:center}
.patient-center h2{font-size:30px;width:372px}
.post-date{font-size:11px;font-style:italic}
.post-title{font-family:'Raleway',sans-serif;font-size:15px;line-height:1.4;margin-top:4px;width:690px}

/* testimonials */
.team-photo{position:absolute;top:1618px;left:0;width:600px;height:392px;background:linear-gradient(180deg,#7d8a6f 0%,#5a6a63 45%,#2e3750 100%)}
.testimonials{position:absolute;top:1618px;left:600px;width:600px;height:392px;padding:56px 38px}
.testimonials h2{font-size:30px}
.slider-arrows{position:absolute;right:40px;top:62px;display:flex;gap:6px}
.slider-arrows span{width:28px;height:28px;border:1px solid #bbb;display:flex;align-items:center;justify-content:center}
.stars{color:#f2c300;font-size:11px;letter-spacing:1px;margin-top:24px}
.quote{font-size:10.5px;font-style:italic;line-height:1.65;color:#444;margin-top:8px}
.reviewer{display:flex;align-items:center;gap:10px;font-size:11px;margin-top:14px}
.avatar{width:26px;height:26px;border-radius:50%;background:#9a8f86}
.testimonials .btn{margin-top:56px}

/* eyewear */
.frames{position:absolute;top:2010px;left:0;width:1200px;height:218px;display:flex;justify-content:space-between;padding:0 45px;align-items:center}
.frame{width:290px;height:120px;background:linear-gradient(180deg,#fafafa,#e9e9e9)}
.labels{position:absolute;top:2268px;left:0;width:1200px;height:100px;display:flex;justify-content:space-between;align-items:center;padding:0 22px;font-family:'Lato',sans-serif;font-weight:700;font-size:19px;color:#111}

/* footer */
.site-footer{position:absolute;top:2398px;left:0;width:1200px;height:324px;background:var(--darker);color:var(--white)}
.footer-brand{position:absolute;left:38px;top:60px}
.footer-brand .brand-name{color:var(--yellow)}
.footer-brand p{font-size:10px;line-height:1.7;width:220px;margin-top:28px;color:#ddd}
.socials{display:flex;gap:10px;margin-top:18px}
.socials span{width:28px;height:28px;border-radius:50%;border:1px solid #555}
.footer-col{position:absolute;top:70px;width:185px;font-size:10px;line-height:1.5;color:#ddd}
.footer-col h3{font-family:'Raleway',sans-serif;font-weight:500;font-size:12px;letter-spacing:.2px;white-space:nowrap;color:var(--white);margin-bottom:16px;text-transform:uppercase}
.footer-col li{list-style:none;display:flex;gap:9px;margin-bottom:12px}
.footer-col.links li{margin-bottom:9px}
.badges{position:absolute;left:910px;top:60px;display:flex;flex-direction:column;gap:40px}
.badge{width:140px;height:46px;border-radius:3px;background:#3a3a3a}
.bottom-bar{position:absolute;top:2722px;left:0;width:1200px;height:39px;background:var(--yellow);display:flex;justify-content:space-between;align-items:center;padding:0 38px;font-size:10px}
</style>
</head>
<body>

<header class="site-header">
  <div class="brand"><span class="brand-mark"></span><span class="brand-name">BRINDLE COVE<br>OPTOMETRY</span></div>
  <div class="top-contact">
    <span><svg width="10" height="10" viewBox="0 0 24 24"><path fill="#444" d="M6.6 10.8a15 15 0 006.6 6.6l2.2-2.2a1 1 0 011-.2 11 11 0 003.6.6 1 1 0 011 1V20a1 1 0 01-1 1A17 17 0 013 4a1 1 0 011-1h3.5a1 1 0 011 1 11 11 0 00.6 3.6 1 1 0 01-.3 1z"/></svg> 555-201-4410</span>
    <span class="btn">Make an Appointment</span>
  </div>
  <nav class="main-nav">
    <span>Home</span><span>About Us ▾</span><span>Eyecare ▾</span><span>Dry Eye Clinic</span><span>Patient Center ▾</span><span>Promotions</span><span>Brands ▾</span><span>Testimonials</span><span>Find Us</span>
  </nav>
</header>

<section class="hero" role="img" aria-label="Photo of a smiling girl covering one eye during an eye exam with her mother, beside an eye examination instrument">
  <div class="hero-copy">
    <h1>TOTAL<br>EYE CARE<br>SOLUTION</h1>
    <p>Lorem ipsum dolor sit amet, an pro accusam perfecto, vim malis incorrupte reformidans id, ex pri justo voluptatum.</p>
    <span class="btn">Learn More</span>
  </div>
</section>

<section class="info-row">
  <div class="promise">
    <h2 class="heading">THE BRINDLE COVE PROMISE</h2>
    <div class="rule"></div>
    <p>Welcome to Brindle Cove Optometry, where your vision and eye health are our sole priority. We take great pride in providing you with state-of-the-art eyecare matched with personal attention from our staff and doctors. Your quality of life is our goal and we believe that healthy eyesight is vital to achieving it.</p>
    <p>Our professional and personable staff is highly trained in helping you achieve and maintain healthy eyesight. Our optometrists have combined experiences and specialize in Orthokeratology (OrthoK), Ocular disease, Glaucoma diagnosis &amp; management.</p>
    <span class="btn">About Us</span>
  </div>
  <div class="hours">
    <h2 class="heading">HOURS</h2>
    <div class="rule"></div>
    <table>
      <tr><td>Monday - Thursday</td><td>9:00 AM - 6:00 PM</td></tr>
      <tr><td>Friday</td><td>8.30 AM - 5:00 PM</td></tr>
      <tr><td>Saturday</td><td>8.30 AM - 5:00 PM</td></tr>
    </table>
    <p class="note">Closed on Sundays<br><br>Please keep in mind we are closed for lunch<br>1:00 PM - 2:00 PM</p>
  </div>
  <div class="find">
    <h2 class="heading">FIND US</h2>
    <div class="rule"></div>
    <ul>
      <li><svg width="10" height="12" viewBox="0 0 24 24"><path fill="#fff" d="M12 2a7 7 0 00-7 7c0 5 7 13 7 13s7-8 7-13a7 7 0 00-7-7zm0 9.5A2.5 2.5 0 1112 6.5a2.5 2.5 0 010 5z"/></svg><span>4820 Larkmoor Ave,<br>Fernhollow, CA 90000</span></li>
      <li><svg width="10" height="10" viewBox="0 0 24 24"><path fill="#fff" d="M6.6 10.8a15 15 0 006.6 6.6l2.2-2.2a1 1 0 011-.2 11 11 0 003.6.6 1 1 0 011 1V20a1 1 0 01-1 1A17 17 0 013 4a1 1 0 011-1h3.5a1 1 0 011 1 11 11 0 00.6 3.6 1 1 0 01-.3 1z"/></svg><span>555-201-4410</span></li>
      <li><svg width="10" height="10" viewBox="0 0 24 24"><rect x="5" y="2" width="14" height="7" fill="#fff"/><rect x="2" y="10" width="20" height="9" fill="#fff"/></svg><span>555-201-4470</span></li>
      <li><svg width="11" height="10" viewBox="0 0 24 24"><path fill="none" stroke="#fff" stroke-width="2" d="M3 5h18v14H3zM3 5l9 8 9-8"/></svg><span>info@brindlecove.com</span></li>
    </ul>
    <span class="btn">View All Locations</span>
  </div>
</section>

<section class="services">
  <div class="tile"><div class="tile-card">Myopia<br>Control<br>Clinic</div></div>
  <div class="ph" role="img" aria-label="Photo of a tired office worker rubbing her eyes at a desk" style="background:linear-gradient(180deg,#f3f3f3,#dcdcdc)"></div>
  <div class="tile"><div class="tile-card">Dry Eye<br>Clinic</div></div>
  <div class="ph" role="img" aria-label="Close-up photo of an eye with dry skin around it" style="background:linear-gradient(160deg,#c9ad8e 0%,#b59a7c 50%,#a88c70 100%)"></div>
  <div class="ph" role="img" aria-label="Photo of a child wearing a trial frame during an eye test" style="background:linear-gradient(120deg,#3f5a86,#d9b9a0 55%,#f0e3d8)"></div>
  <div class="tile"><div class="tile-card">Eyecare</div></div>
  <div class="ph" role="img" aria-label="Close-up photo of a contact lens on a fingertip near an eye" style="background:linear-gradient(150deg,#e9d6cc,#cfae9c 60%,#b99384)"></div>
  <div class="tile"><div class="tile-card">Contact<br>Lenses</div></div>
</section>

<section class="patient-center">
  <div><h2 class="heading">PATIENT CENTER</h2><div class="rule"></div></div>
  <div>
    <div class="post-date">19 February, 2019</div>
    <div class="post-title">Lorem ipsum dolor sit amet, ea eam partem aperiri epicurei, simul atomorum ius ad dolore sensi bus honestatis cu quo</div>
  </div>
</section>

<div class="team-photo" role="img" aria-label="Group photo of the practice team standing in the clinic reception"></div>
<section class="testimonials">
  <h2 class="heading">TESTIMONIALS</h2>
  <div class="rule" style="background:#ccc"></div>
  <div class="slider-arrows">
    <span><svg width="10" height="8" viewBox="0 0 10 8"><path d="M4 0L0 4l4 4M0 4h10" fill="none" stroke="#444"/></svg></span>
    <span><svg width="10" height="8" viewBox="0 0 10 8"><path d="M6 0l4 4-4 4M10 4H0" fill="none" stroke="#444"/></svg></span>
  </div>
  <div class="stars">★★★★★</div>
  <p class="quote">Excellent experience here today. Definitely recommend. Highly efficient staff (also friendly and super respectful) awesome optometrist, parking is free. Pricing came out way better than I was expecting. Yay, New Glasses!</p>
  <div class="reviewer"><span class="avatar"></span>Dana Whitfield</div>
  <span class="btn">View All Testimonials</span>
</section>

<section class="frames">
  <div class="frame" role="img" aria-label="Photo of black rectangular eyeglass frames"></div>
  <div class="frame" role="img" aria-label="Photo of grey metal eyeglass frames"></div>
  <div class="frame" role="img" aria-label="Photo of black cat-eye eyeglass frames"></div>
</section>

<section class="labels">
  <span>MARLOWE FINCH</span><span>STRIDE</span><span>KIRO HANAYA</span><span>VELMONT</span><span>OUTLINE</span><span>nord frame</span><span>Belcour</span>
</section>

<footer class="site-footer">
  <div class="footer-brand">
    <div class="brand" style="position:static"><span class="brand-mark"></span><span class="brand-name">BRINDLE COVE<br>OPTOMETRY</span></div>
    <p>Lorem ipsum dolor sit amet, ei vix iusto dolore delicatissimi at ullum nostro vel.</p>
    <div class="socials"><span></span><span></span><span></span><span></span></div>
  </div>
  <div class="footer-col" style="left:308px">
    <h3>Brindle Cove Optometry</h3>
    <ul>
      <li>◦<span>4820 Larkmoor Ave,<br>Fernhollow, CA 90000</span></li>
      <li>◦<span>555-201-4410</span></li>
      <li>◦<span>555-201-4470</span></li>
      <li>◦<span>info@brindlecove.com</span></li>
    </ul>
  </div>
  <div class="footer-col" style="left:510px">
    <h3>Alder Ridge</h3>
    <ul>
      <li>◦<span>1290 Quillfield St., Suite 4,<br>Alder Ridge, CA 90001</span></li>
      <li>◦<span>555-208-3320</span></li>
      <li>◦<span>alderridge@brindlecove.com</span></li>
    </ul>
  </div>
  <div class="footer-col links" style="left:708px">
    <h3>Information</h3>
    <ul><li>About Us</li><li>Services</li><li>Locations</li><li>Patient Center</li><li>Team</li><li>Career</li></ul>
  </div>
  <div class="badges">
    <div class="badge" style="background:#f2f2f2"></div>
    <div class="badge"></div>
    <div class="badge"></div>
  </div>
</footer>

<div class="bottom-bar">
  <span>Copyright © 2019 Brindle Cove Optometry</span>
  <span>↑ Back To Top</span>
</div>

</body>
</html>
```